Etiketten für Kosmetik Produkte  100% Natural Made in Germany
Etiketten für Kosmetik Produkte 100% Natural Made in Germany
Zielgruppe
auf Hochwertige -zertifizierte Naturprodukte wert legen.
Hergestellt in Deutschland und Verpackt
Aufgabenstellung
Hallo ihr lieben,
für die SilbTau Kosmetik - wünschen wir einen neuen frischen Style - das dunkle Etikett möchten wir los werden.
Ein helles frisches Design
Zielgruppe- alle die auf Hochwertige - zertifizierte Naturprodukte bevorzugen
Die Produkte haben mit eine VERUN Zertifizierung - Höchste Qalität an Naturprodukte
Das Glas was wir nutzen ist ein violettes Glas und sehr hochwertig was wir beibehalten möchten.
Das Produkt ist dadurch sehr Geschütz und nachhaltig dazu
Es sind 12 Produkte - Design bleibt bei allen gleich.
Design Wunsch -!!!!
Was gut zum Glas Passt- nur kein schwarz bitte
und Produkt gut passt
Weiß - Kupfer eventuell
Kein Muss - sind für alles offen ( nur kein schwarz
Logo - Name bleibt :-)
Das Design von Tesoro Naturkosmetik
Gefällt uns sehr gut in der Richtung
Was die Natürlichkeit- Reinheit - Qualität
Verkörpert:-)
Fotos zum Prosukt:
Hier ein link zum Instagram
https://instagram.com/lumaroze.spain?igshid=MzRlODBiNWFlZA==
https://instagram.com/silbtau_naturkosmetik?igshid=MzRlODBiNWFlZA==
An den Flyer den wir hochgeladen kann man sehen um welche Produkte es sich handelt und auch im Instagram zu sehen sind.
Wenn ihr weitere Fotos benötigen tut- bitte melden
Viel Glück :-) danke für eure Unterstützung

```html
<!DOCTYPE html>
<html lang="de">
<head>
<meta charset="utf-8">
<title>SilbTau Naturkosmetik – Lemon &amp; Orange Body Oil</title>
<link rel="stylesheet" href="https://fonts.googleapis.com/css2?family=Playfair+Display:wght@400;700&family=Montserrat:wght@400;600;700&family=Roboto+Condensed:wght@400;500;700&display=swap">
<style>
  :root {
    --bg: #e3e4e8;
    --paper: #ffffff;
    --side-paper: #f3f3f4;
    --copper: #c27f58;
    --copper-deep: #a85f3a;
    --copper-soft: #d6a486;
    --ink: #3a3634;
    --ink-soft: #6e6865;
  }
  * { box-sizing: border-box; margin: 0; padding: 0; }
  html, body { width: 1200px; height: 1047px; overflow: hidden; }
  body { background: var(--bg); font-family: "Montserrat", sans-serif; color: var(--ink); position: relative; }

  .brand { text-align: center; color: var(--copper); font-family: "Playfair Display", serif; font-weight: 400; }
  .brand-dot { display: block; margin: 0 auto 6px; border: 1.5px solid var(--copper); border-radius: 50%; }
  .brand-name { display: block; letter-spacing: 0.02em; line-height: 1; }
  .brand-sub { display: block; letter-spacing: 0.04em; margin-top: 3px; }

  .title { font-family: "Playfair Display", serif; font-weight: 700; color: var(--copper); line-height: 1.02; }
  .claims { color: var(--ink-soft); line-height: 1.4; }
  .rule { height: 1.5px; background: var(--copper); }
  .made { font-weight: 700; color: var(--ink); letter-spacing: 0.02em; line-height: 1.45; }
  .band { background: linear-gradient(90deg, var(--copper-deep), var(--copper), var(--copper-deep)); color: #fff; font-weight: 600; letter-spacing: 0.18em; text-align: center; position: absolute; left: 0; right: 0; }

  /* Bottle label */
  .bottle-label { position: absolute; left: 80px; top: 300px; width: 340px; height: 440px; background: var(--paper); box-shadow: 0 12px 30px rgba(0,0,0,0.08); }
  .bottle-label .brand { margin-top: 28px; }
  .bottle-label .brand-dot { width: 34px; height: 34px; }
  .bottle-label .brand-name { font-size: 24px; }
  .bottle-label .brand-sub { font-size: 12px; }
  .bottle-label .content { padding: 0 36px; }
  .bottle-label .title { font-size: 40px; margin-top: 36px; }
  .bottle-label .claims { font-size: 13px; margin-top: 26px; }
  .bottle-label .rule { width: 60px; margin: 12px 0 14px; }
  .bottle-label .made { font-size: 10px; }
  .bottle-label .band { bottom: 0; height: 38px; line-height: 38px; font-size: 14px; }

  /* Box */
  .box { position: absolute; left: 470px; top: 110px; display: flex; box-shadow: 0 14px 36px rgba(0,0,0,0.08); }
  .box-front { position: relative; width: 340px; height: 830px; background: var(--paper); }
  .box-front .brand { margin-top: 72px; }
  .box-front .brand-dot { width: 40px; height: 40px; }
  .box-front .brand-name { font-size: 30px; }
  .box-front .brand-sub { font-size: 14px; }
  .box-front .content { position: absolute; left: 40px; right: 30px; top: 430px; }
  .box-front .title { font-size: 52px; }
  .box-front .claims { font-size: 15px; margin-top: 28px; color: var(--ink); }
  .box-front .rule { width: 70px; margin: 14px 0 16px; }
  .box-front .made { font-size: 12px; }
  .box-front .band { bottom: 0; height: 52px; line-height: 52px; font-size: 16px; }

  .box-side { position: relative; width: 240px; height: 830px; background: var(--side-paper); border-left: 1px solid #e2e2e4; font-family: "Roboto Condensed", sans-serif; color: var(--ink); padding: 220px 22px 0 22px; }
  .box-side p { font-size: 13px; line-height: 1.45; }
  .box-side .intro { font-weight: 500; }
  .box-side h3 { font-size: 13px; font-weight: 700; margin: 20px 0 2px; }
  .box-side .footnote { font-size: 10px; margin-top: 22px; color: var(--ink-soft); }
  .box-side .band { bottom: 0; height: 52px; }
</style>
</head>
<body>

  <section class="bottle-label" aria-label="Flaschenetikett">
    <div class="brand">
      <span class="brand-dot"></span>
      <span class="brand-name">SILBTAU</span>
      <span class="brand-sub">NATURKOSMETIK</span>
    </div>
    <div class="content">
      <h1 class="title">Lemon &amp;<br>Orange<br>Body Oil</h1>
      <p class="claims">Organic • Vegan<br>Cruelty free • 100% Natural</p>
      <div class="rule"></div>
      <p class="made">MADE IN GERMANY<br>DERMATOLOGISCH GETESTET</p>
    </div>
    <div class="band">BODY CARE</div>
  </section>

  <section class="box" aria-label="Faltschachtel">
    <div class="box-front">
      <div class="brand">
        <span class="brand-dot"></span>
        <span class="brand-name">SILBTAU</span>
        <span class="brand-sub">NATURKOSMETIK</span>
      </div>
      <div class="content">
        <h2 class="title">Lemon &amp;<br>Orange<br>Body Oil</h2>
        <p class="claims">Organic • Vegan<br>Cruelty free • 100% Natural</p>
        <div class="rule"></div>
        <p class="made">MADE IN GERMANY<br>DERMATOLOGISCH GETESTET</p>
      </div>
      <div class="band">BODY CARE</div>
    </div>

    <div class="box-side">
      <p class="intro">Wertvolles Körperöl mit Orangen- und Zitronenöl, für erfrischende Momente. Naturreines Mandel-, Jojoba- und Sheaöl aus kontrolliert biologischem Anbau pflegen die Haut auf wohltuende Weise.</p>
      <h3>ANWENDUNG</h3>
      <p>LEMON &amp; ORANGE OIL sparsam nach dem Duschen oder Baden auf die feuchte Haut auftragen und einmassieren. Bereits geringe Mengen der rein pflanzlichen Pflegekomposition pflegen die Haut natürlich schön.</p>
      <h3>INGREDIENTS</h3>
      <p>Simmondsia Chinensis Seed Oil*, Prunus Amygdalus Dulcis Oil*, Helianthus Annuus Seed Oil*, Argania Spinosa Kernel Oil*, Butyrospermum Parkii Nut Extract*, Tocopherol, Citrus Limon Peel Oil*, Citrus Aurantium Dulcis Peel Oil*</p>
      <p class="footnote">*Rohstoffe aus kontrolliert<br>Biologischem Anbau</p>
      <div class="band"></div>
    </div>
  </section>

</body>
</html>
```